Pelmora needs stationery design

We need desings for presentation cards and letter head for our company. It would be better that the letterhead uses our logo with white background and the presentation card the logo with the black background for the back of the card and the text (name, phone
Updates

Necesitas un par de días antes de escoger al ganador

Colors
0455a3
ec1f27
000000

Requirements
Must have
• Use company logo and colors

```html
<!DOCTYPE html>
<html lang="en">
<head>
<meta charset="utf-8">
<title>Pelmora Business Card</title>
<link rel="stylesheet" href="https://fonts.googleapis.com/css2?family=Roboto:wght@300;400;700&display=swap">
<style>
  :root {
    --brand-blue: #0455a3;
    --card-blue: #0a63c4;
    --brand-red: #ec1f27;
    --card-black: #1b1c1e;
    --white: #ffffff;
    --soft-white: #e6eef8;
    --stage: #e9e7e4;
  }
  * { box-sizing: border-box; margin: 0; padding: 0; }
  html, body {
    width: 1200px; height: 960px; overflow: hidden;
    background: var(--stage);
    font-family: "Roboto", Arial, sans-serif;
  }
  .sheet {
    position: relative; width: 1200px; height: 960px;
    display: flex; flex-direction: column; align-items: center; justify-content: center; gap: 60px;
  }
  .card {
    position: relative; width: 620px; height: 354px;
    background: var(--card-black); overflow: hidden;
    box-shadow: 0 6px 18px rgba(0,0,0,0.18);
  }
  .wordmark {
    position: absolute;
    color: var(--white); font-weight: 300; text-transform: uppercase;
    letter-spacing: 0.12em; line-height: 1;
  }
  .card--front .wordmark { font-size: 58px; left: 50%; top: 50%; transform: translate(-50%, -50%); }
  .card--back .wordmark { font-size: 40px; left: 40px; top: 196px; }
  .card__divider { position: absolute; inset: 0; width: 620px; height: 354px; }
  .contact {
    position: absolute; left: 348px; top: 48px; color: var(--white);
  }
  .contact__name { font-size: 22px; font-weight: 700; letter-spacing: 0.01em; text-transform: uppercase; }
  .contact__title { font-size: 15px; font-weight: 300; text-transform: uppercase; margin-top: 2px; }
  .contact__address { font-size: 12.5px; font-weight: 300; color: var(--soft-white); margin-top: 14px; line-height: 1.45; }
  .contact__list { list-style: none; margin-top: 16px; font-size: 12.5px; font-weight: 300; color: var(--soft-white); }
  .contact__list li { display: flex; align-items: center; gap: 10px; line-height: 1.75; }
  .contact__icon { width: 12px; height: 12px; fill: var(--white); flex: none; }
</style>
</head>
<body>
<main class="sheet">
  <section class="card card--front" aria-label="Card front">
    <span class="wordmark">Pelmora</span>
  </section>

  <section class="card card--back" aria-label="Card back">
    <svg class="card__divider" viewBox="0 0 620 354" aria-hidden="true">
      <path d="M292 0 H620 V354 H292 V112 L312 92 L312 78 Z" fill="var(--card-blue)"/>
      <path d="M292 0 V354" stroke="none"/>
      <path d="M292 0 V72 L312 78 L312 92 L292 112 V354" fill="none" stroke="var(--brand-red)" stroke-width="3"/>
    </svg>
    <span class="wordmark">Pelmora</span>
    <div class="contact">
      <p class="contact__name">Dana Reyes</p>
      <p class="contact__title">CEO/Founder</p>
      <p class="contact__address">214 Harbor Street<br>Fairview, Oregon 97024</p>
      <ul class="contact__list">
        <li><svg class="contact__icon" viewBox="0 0 12 12"><path d="M2.5 0.5 L4.5 3 L3.5 4.5 Q4.5 7 7.5 8.5 L9 7.5 L11.5 9.5 L10 11.5 Q5 11.5 0.5 2 Z"/></svg>541 208 7731</li>
        <li><svg class="contact__icon" viewBox="0 0 12 12"><path d="M3 0 H9 V12 H3 Z M4 1.5 V9.5 H8 V1.5 Z"/></svg>541 377 6120</li>
        <li><svg class="contact__icon" viewBox="0 0 12 12"><path d="M3 0 H9 V3 H3 Z M0.5 4 H11.5 V10 H9 V12 H3 V10 H0.5 Z M4 8 V11 H8 V8 Z"/></svg>541 903 4458</li>
        <li><svg class="contact__icon" viewBox="0 0 12 12"><path d="M0.5 2 H11.5 V10 H0.5 Z M1.5 3 L6 6.5 L10.5 3 Z" fill-rule="evenodd"/></svg>hello@pelmora.com</li>
        <li><svg class="contact__icon" viewBox="0 0 12 12"><circle cx="6" cy="6" r="5.5"/><path d="M0.5 6 H11.5 M6 0.5 Q3 6 6 11.5 M6 0.5 Q9 6 6 11.5" stroke="var(--card-blue)" fill="none" stroke-width="0.9"/></svg>www.pelmora.com</li>
      </ul>
    </div>
  </section>
</main>
</body>
</html>
```